Venmark Power Web Design

I want a design for a home page that can function as a template for the entire web design. I"m also requesting that the design be adapted as a template for Power Point presentations, as well.

Here"s a brief about our company:

Venmark Power provides its customers with clean, redundant and reliable power. Functioning as a private power producer, Venmark Power owns and operates combined heat and power (CHP) and distributed generation (DG) systems.

Venmark’s management has extensive experience in aerospace turbines engine operation, maintenance, manufacturing and repair. Depending on the customer need, Venmark either builds new generators or refurbish “retired” aerospace turbines into industrial generators. This allows Venmark to deliver generating systems at greatly reduced capital outlays, enabling Venmark Power to offer its customers not only redundant power and grid independence, but significant savings on their energy needs. Venmark’s typical installation size is 500Kws to 3Mws but based upon our customer"s needs, Venmark can site multiple generators to configure systems of larger size.

By using aero derivative turbine engines the company has the flexibility to use the best source of fuel for each site and power requirement. The turbine engine can operate on virtually any combustible fuel. This allows Venmark to utilize the flex fuel practice and operate on either the least expensive fuel available or operate on renewable and biofuels to fulfill the green power requirements mandated by many federal, state and local utility commissions.

Venmark’s market strategy is as follows:

1. Sell reliable and redundant power through a PPAs or lease agreements to industrial or institutional customers with high electrical and thermal needs such as food processors, bio fuel producers, hospitals, casinos, hotels, etc.

2. Lease its systems to customer that “flare gas” as byproducts of their processes such as wastewater treatment facilities, land fills and "stranded gas wells" allowing them to use their waste products to power their facilities and sell excess electricity back to the grid.

3. Partner with other private power producers to provide the turbine generating capacity on a leased basis.
Updates

Please disregard the "turbine logo" that was uploaded as a file and focus only on the "bolt design logo", A (bolt) E.

We like the simple navigation and clean and modern design of sites.

http://www.plusoria.example/

http://www.gravunet.example/

http://www.tovelspace.example/

Target Market(s)

Our target markets can be found on the web architecture file I've attached to this submission.

Number of Pages Required

1 page

Requirements
Must have
• The designer must provide a web design and a Power Point template based upon the web design.

• The design must contemplate the web architecture that I""ve included as a file.

```html
<!DOCTYPE html>
<html lang="en">
<head>
<meta charset="utf-8">
<title>Venmark Power – Web and Slide Templates</title>
<link href="https://fonts.googleapis.com/css2?family=Arimo:wght@400;700&display=swap" rel="stylesheet">
<style>
:root{
  --lime:#c9dc2a;
  --brand:#2e9e3a;
  --olive:#6b7a12;
  --earth-dark:#574300;
  --muted:#a99b9b;
  --body:#8a8a8a;
  --orange:#f47c1c;
  --white:#ffffff;
  --frame:#9a9a9a;
  --photo-top:#e4ebe0;
  --photo-mid:#93b978;
  --photo-low:#557c98;
}
*{box-sizing:border-box;margin:0;padding:0}
html,body{width:866px;height:1200px;overflow:hidden;background:var(--white)}
body{position:relative;font-family:'Arimo',Arial,sans-serif}
.abs{position:absolute}
.brand{display:flex;align-items:center;gap:5px;color:var(--brand);font-weight:700;white-space:nowrap}
.brand .dot{width:8px;height:8px;border-radius:50%;background:var(--lime)}
.photo{position:absolute;background:linear-gradient(180deg,var(--photo-top) 0%,var(--photo-mid) 50%,var(--photo-low) 100%)}
.photo-hands{position:absolute;background:linear-gradient(180deg,#5a9e3c 0%,#8a6a40 45%,#e0b596 100%)}
.photo-earth{position:absolute;background:linear-gradient(135deg,#c9d7de 0%,#6f9478 45%,#3d6aa0 100%)}
/* nav */
.nav{left:401px;top:21px;display:flex;gap:2px}
.nav a{width:58px;height:56px;background:var(--lime);color:var(--white);font-size:7.5px;text-decoration:none;display:flex;align-items:center;justify-content:center;text-align:center;line-height:1.05}
/* hero */
.hero{left:22px;top:96px;width:814px;height:168px;background:radial-gradient(ellipse 70% 90% at 60% 20%,#ffffff 40%,#eeeeee 100%)}
.hero h1{position:absolute;left:478px;top:38px;font-size:15px;font-weight:400;color:var(--olive);white-space:nowrap}
.hero p{position:absolute;left:478px;top:58px;width:222px;font-size:7.4px;line-height:13px;color:#777;text-align:justify}
.btn{position:absolute;left:479px;top:110px;width:86px;height:22px;border-radius:11px;background:linear-gradient(#ff9a3a,var(--orange));color:var(--white);font-size:8px;display:flex;align-items:center;justify-content:center;box-shadow:0 3px 4px rgba(0,0,0,.2)}
/* features */
.feature h2{font-size:14px;font-weight:400;color:var(--muted);position:absolute;top:0;white-space:nowrap}
.feature p{position:absolute;left:70px;top:32px;width:108px;font-size:7px;line-height:11.5px;color:var(--body);text-align:justify}
.feature .more{position:absolute;left:122px;top:74px;font-size:7px;color:var(--lime);display:flex;align-items:center;gap:4px;white-space:nowrap}
.feature .more i{width:9px;height:9px;border-radius:50%;background:#444;display:inline-block}
.feature svg{position:absolute;left:-2px;top:24px}
/* sitemap band */
.sitemap{left:22px;top:385px;width:814px;height:127px;background:var(--lime)}
.col{position:absolute;top:13px;color:var(--white)}
.col h3{font-size:15px;font-weight:400;margin-bottom:9px;white-space:nowrap}
.col li{list-style:none;font-size:8.5px;line-height:15.4px;padding-left:8px;position:relative;white-space:nowrap}
.col li::before{content:"";position:absolute;left:0;top:4px;border-left:4px solid #eef5a8;border-top:2.5px solid transparent;border-bottom:2.5px solid transparent}
.legal{left:22px;top:512px;width:814px;height:28px;background:var(--earth-dark);font-size:7.5px;color:var(--lime)}
.legal span{position:absolute;top:9px;white-space:nowrap}
/* slides */
.slide{width:396px;height:298px;border:1px solid var(--frame);overflow:hidden;background:var(--white)}
.slide .strip{position:absolute;left:0;bottom:0;width:100%;height:14px;background:var(--lime)}
.ghost{color:#e4e4e4;font-size:30px;font-weight:400;white-space:nowrap}
</style>
</head>
<body>

<!-- Home page -->
<div class="abs brand" style="left:150px;top:52px;font-size:14px"><span class="dot"></span>Venmark Power</div>

<nav class="abs nav">
  <a href="#">ABOUT<br>VENMARK</a><a href="#">CHP</a><a href="#">STRANDED<br>GAS</a><a href="#">RESOURCES</a><a href="#">PARTNER<br>&amp; SUPPLIER</a><a href="#">CONTACT<br>US</a>
</nav>

<section class="abs hero">
  <div class="photo" role="img" aria-label="Light bulb with a green plant inside, standing on the globe" style="left:140px;top:8px;width:300px;height:160px"></div>
  <h1>Lorem ipsum dolor sit amet.</h1>
  <p>Lorem ipsum dolor sit amet, consectetur adipiscing elit. Cras blandit ullamcorper erat, ac dictum augue egestas sit amet. Maecenas neque nisl,</p>
  <div class="btn">VIEW ABOUT US</div>
</section>

<div class="abs feature" style="left:160px;top:274px;width:180px;height:92px">
  <h2>What is CHP</h2>
  <svg width="54" height="46" viewBox="0 0 54 46"><path d="M4 22 L27 4 L50 22" fill="none" stroke="#2e9e3a" stroke-width="4"/><rect x="10" y="20" width="34" height="24" fill="#7cc142"/><circle cx="27" cy="32" r="7" fill="#fff"/></svg>
  <p>Lorem ipsum dolor sit amet, consectetur adipiscing elit. Donec a velit eros,</p>
  <div class="more"><i></i>Read More</div>
</div>
<div class="abs feature" style="left:365px;top:275px;width:180px;height:92px">
  <h2>Stranded Gas</h2>
  <svg width="46" height="46" viewBox="0 0 46 46"><circle cx="20" cy="26" r="16" fill="none" stroke="#2e9e3a" stroke-width="4"/><ellipse cx="20" cy="26" rx="7" ry="16" fill="none" stroke="#2e9e3a" stroke-width="2"/><line x1="4" y1="26" x2="36" y2="26" stroke="#2e9e3a" stroke-width="2"/><path d="M30 14 Q34 2 44 4 Q42 14 30 14Z" fill="#7cc142"/></svg>
  <p>Lorem ipsum dolor sit amet, consectetur adipiscing elit. Donec a velit eros,</p>
  <div class="more"><i></i>Read More</div>
</div>
<div class="abs feature" style="left:567px;top:275px;width:180px;height:92px">
  <h2>Resources</h2>
  <svg width="40" height="48" viewBox="0 0 40 48"><line x1="20" y1="6" x2="20" y2="46" stroke="#2e9e3a" stroke-width="3"/><g fill="#3a9a2a"><ellipse cx="13" cy="16" rx="6" ry="4"/><ellipse cx="27" cy="16" rx="6" ry="4"/><ellipse cx="13" cy="27" rx="6" ry="4"/><ellipse cx="27" cy="27" rx="6" ry="4"/><ellipse cx="13" cy="38" rx="6" ry="4"/><ellipse cx="27" cy="38" rx="6" ry="4"/><ellipse cx="20" cy="6" rx="3" ry="5" fill="#7cc142"/></g></svg>
  <p>Lorem ipsum dolor sit amet, consectetur adipiscing elit. Donec a velit eros,</p>
  <div class="more"><i></i>Read More</div>
</div>

<section class="abs sitemap">
  <div class="col" style="left:140px"><h3>CHP</h3><ul><li>What is CHP?</li><li>Benefits</li><li>Energy Security</li><li>Markets</li></ul></div>
  <div class="col" style="left:247px"><h3>Stranded Gas</h3><ul><li>Benefits</li><li>Energy Security</li><li>Markets</li></ul></div>
  <div class="col" style="left:373px"><h3>Resources</h3><ul><li>ERB</li><li>CQA</li><li>Gulf Coast</li><li>Application Center</li><li>Etc</li></ul></div>
  <div class="col" style="left:493px"><h3>Partner &amp; Supplies</h3><ul><li>Harlow &amp; Pike (help)</li><li>Lorem Ipsum</li><li>Dolor Ipsum</li></ul></div>
  <div class="photo-hands" role="img" aria-label="Cupped hands holding a young plant in soil" style="left:650px;top:12px;width:84px;height:102px"></div>
</section>
<footer class="abs legal">
  <span style="left:135px">Texas CHP Critical Infrastructure legislation</span>
  <span style="left:299px">|</span>
  <span style="left:318px">Is your business a good candidate for CHP</span>
  <span style="left:482px">|</span>
  <span style="left:504px">CHP Calculator</span>
  <span style="left:590px;top:8px;color:var(--white);font-size:8.5px">Copyright 2010. Venmark Power</span>
</footer>

<!-- Slide templates -->
<div class="abs slide" style="left:22px;top:562px">
  <div class="abs brand" style="left:128px;top:96px;font-size:13px"><span class="dot"></span>Venmark Power</div>
  <div class="photo" role="img" aria-label="Light bulb with a green plant inside, standing on the globe" style="left:42px;top:138px;width:312px;height:146px"></div>
  <div class="strip"></div>
</div>

<div class="abs slide" style="left:437px;top:563px">
  <div class="abs brand" style="left:19px;top:50px;font-size:12px"><span class="dot"></span>Venmark Power</div>
  <div class="abs ghost" style="left:182px;top:170px">Venmark Power</div>
  <div class="photo" role="img" aria-label="Light bulb with a plant on the edge of the globe" style="left:0;top:160px;width:121px;height:124px"></div>
  <div class="strip"></div>
  <div class="abs" style="left:357px;bottom:0;width:20px;height:16px;background:var(--earth-dark)"></div>
</div>

<div class="abs slide" style="left:22px;top:882px">
  <div class="abs" style="left:0;top:0;width:57px;height:100%;background:var(--lime)"></div>
  <div class="photo" role="img" aria-label="Light bulb with a green plant inside" style="left:24px;top:79px;width:60px;height:103px"></div>
  <div class="abs brand" style="left:96px;top:124px;font-size:11px"><span class="dot"></span>Venmark Power</div>
  <div class="photo-earth" role="img" aria-label="Part of the globe seen from space" style="left:272px;top:220px;width:124px;height:78px"></div>
</div>

<div class="abs slide" style="left:442px;top:882px">
  <div class="abs" style="left:0;top:101px;width:100%;height:103px;background:var(--lime)"></div>
  <div class="photo" role="img" aria-label="Light bulb with a green plant inside, standing on the globe" style="left:104px;top:108px;width:192px;height:96px"></div>
  <div class="abs brand" style="left:144px;top:236px;font-size:12px"><span class="dot"></span>Venmark Power</div>
</div>

</body>
</html>
```